Ridgeway Sparks Business cards

We require somebody to design business cards for our new business.

Target Market(s)

Mining, haulage and civil.

Industry/Entity Type

Auto electrician in mining industry

Contact Information for Business Card

ABN, business email address, mobile number.

Colors
00AB8E
00BBA5
67D7C9
C6EFE9
E9F9F6

Requirements
Must have
• Services I offer: Breakdowns, Field Service, A/C Systems, Machine rewires, mine site vehicle fit outs

```html
<!DOCTYPE html>
<html lang="en">
<head>
<meta charset="utf-8">
<title>Ridgeway Sparks Business Cards</title>
<link href="https://fonts.googleapis.com/css2?family=Roboto:wght@400;500;700&display=swap" rel="stylesheet">
<style>
  :root {
    --teal: #00AB8E;
    --teal-mid: #00BBA5;
    --teal-light: #67D7C9;
    --silver: #b9b9b9;
    --card: #000000;
    --ink: #ffffff;
    --backdrop: #e6e3de;
  }
  html, body {
    margin: 0;
    padding: 0;
    width: 1189px;
    height: 1200px;
    overflow: hidden;
    background: var(--backdrop);
    font-family: "Roboto", Arial, sans-serif;
  }
  .canvas { position: relative; width: 1189px; height: 1200px; }
  .card {
    position: absolute;
    left: 166px;
    width: 860px;
    height: 490px;
    background: var(--card);
    border-radius: 31px;
    overflow: hidden;
    color: var(--ink);
  }
  .card--front { top: 111px; }
  .card--back { top: 643px; }

  .brand {
    position: absolute;
    display: flex;
    flex-direction: column;
    align-items: center;
  }
  .brand__art {
    background: linear-gradient(160deg, var(--teal-light) 0%, var(--teal) 45%, var(--silver) 100%);
    opacity: 0.85;
    border-radius: 4px;
  }
  .brand__name {
    color: var(--teal-mid);
    font-weight: 700;
    font-size: 27px;
    line-height: 1;
    white-space: nowrap;
    margin: 8px 0;
  }
  .card--front .brand { left: 57px; top: 42px; width: 217px; }
  .card--front .brand__art--top { width: 120px; height: 105px; }
  .card--front .brand__art--bottom { width: 175px; height: 70px; }
  .card--back .brand { left: 129px; top: 124px; width: 222px; }
  .card--back .brand__art--top { width: 125px; height: 110px; }
  .card--back .brand__art--bottom { width: 182px; height: 72px; }

  .person {
    position: absolute;
    right: 41px;
    top: 183px;
    text-align: right;
  }
  .person__name {
    color: var(--teal);
    font-weight: 500;
    font-size: 32px;
    line-height: 1.1;
  }
  .person__role { font-size: 22px; line-height: 1.3; }
  .person-marker {
    position: absolute;
    right: 0;
    top: 186px;
    width: 17px;
    height: 62px;
    background: var(--teal);
  }

  .divider {
    position: absolute;
    left: 61px;
    width: 740px;
    top: 326px;
    height: 2px;
    background: #e5e5e5;
  }

  .contact {
    position: absolute;
    left: 54px;
    top: 344px;
    list-style: none;
    margin: 0;
    padding: 0;
  }
  .contact li {
    display: flex;
    align-items: center;
    height: 37px;
    font-size: 22px;
  }
  .contact svg { width: 22px; height: 22px; margin-right: 13px; fill: var(--teal); }

  .address {
    position: absolute;
    right: 59px;
    top: 346px;
    text-align: right;
    font-size: 22px;
    line-height: 34px;
  }
  .address__abn { color: var(--teal); font-weight: 700; margin-top: 4px; }

  .band {
    position: absolute;
    left: 0; right: 0; bottom: 0;
    height: 12px;
    background: var(--teal);
  }

  .rule-vertical {
    position: absolute;
    left: 389px;
    top: 130px;
    width: 2px;
    height: 230px;
    background: linear-gradient(to bottom, transparent, var(--teal) 20%, var(--teal) 80%, transparent);
  }
  .services { position: absolute; left: 421px; top: 136px; }
  .services__title {
    color: var(--teal);
    font-weight: 500;
    font-size: 27px;
    margin: 0 0 8px;
    line-height: 32px;
  }
  .services__list { list-style: none; margin: 0; padding: 0; }
  .services__list li {
    font-size: 26px;
    line-height: 39.7px;
    position: relative;
    padding-left: 17px;
  }
  .services__list li::before {
    content: "";
    position: absolute;
    left: 0;
    top: 17px;
    width: 6px;
    height: 6px;
    border-radius: 50%;
    background: var(--teal);
  }
</style>
</head>
<body>
<main class="canvas">
  <section class="card card--front">
    <div class="brand">
      <div class="brand__art brand__art--top" role="img" aria-label="Drill rig mast illustration with lightning bolt"></div>
      <div class="brand__name">Ridgeway Sparks</div>
      <div class="brand__art brand__art--bottom" role="img" aria-label="Drilling truck illustration"></div>
    </div>

    <div class="person">
      <div class="person__name">Marcus Hale</div>
      <div class="person__role">Owner</div>
    </div>
    <div class="person-marker"></div>

    <div class="divider"></div>

    <ul class="contact">
      <li>
        <svg viewBox="0 0 24 24" aria-hidden="true"><path d="M7 1h10a2 2 0 0 1 2 2v18a2 2 0 0 1-2 2H7a2 2 0 0 1-2-2V3a2 2 0 0 1 2-2zm0 3v14h10V4zm5 15.5a1 1 0 1 0 0 2 1 1 0 0 0 0-2z"/></svg>
        555.013.2048
      </li>
      <li>
        <svg viewBox="0 0 24 24" aria-hidden="true"><path d="M2 5h20v14H2zm2 2v.5l8 5 8-5V7l-8 5z"/></svg>
        info@webname.com
      </li>
      <li>
        <svg viewBox="0 0 24 24" aria-hidden="true"><path d="M12 1a11 11 0 1 0 0 22 11 11 0 0 0 0-22zm-1 19.9A9 9 0 0 1 4.2 9.5L9 14v1a2 2 0 0 0 2 2zm6.9-2.5A2 2 0 0 0 16 17h-1v-3a1 1 0 0 0-1-1H8v-2h2a1 1 0 0 0 1-1V8h2a2 2 0 0 0 2-2v-.4a9 9 0 0 1 2.9 12.8z"/></svg>
        www.website.com
      </li>
    </ul>

    <div class="address">
      <div>421, Address line goes here</div>
      <div>45452, Country name</div>
      <div class="address__abn">ABN No. 123-456</div>
    </div>

    <div class="band"></div>
  </section>

  <section class="card card--back">
    <div class="brand">
      <div class="brand__art brand__art--top" role="img" aria-label="Drill rig mast illustration with lightning bolt"></div>
      <div class="brand__name">Ridgeway Sparks</div>
      <div class="brand__art brand__art--bottom" role="img" aria-label="Drilling truck illustration"></div>
    </div>

    <div class="rule-vertical"></div>

    <div class="services">
      <h2 class="services__title">SERVICES OFFER</h2>
      <ul class="services__list">
        <li>Breakdowns</li>
        <li>Field Service</li>
        <li>A/C Systems</li>
        <li>Machine rewires</li>
        <li>Mine site vehicle fit outs</li>
      </ul>
    </div>
  </section>
</main>
</body>
</html>
```